Flyer-Design für Seniorenbetreuung
Zielgruppe
Wir sind eine Genossenschaft, welche ihren Immobilienbestand gern erweitern möchte. Dafür soll für unsere Partnerfirma (welche im Seniorenbetreuungssektor tätig ist) eine Flyer erdacht werden, welcher Senioren bzw. ihre Angehörigen anspricht die Wohneigentum besitzen. Viele Senioren besitzen Ein-, Mehrfamilienhäuser oder Eigentumswohnungen und können oder wollen diese nicht weiter vererben. Zusätzlich sind sie durch die Kosten des Eigentums, wie Steuern oder Instandhaltungskosten belastet. Unsere Genossenschaft bietet eine Lösung des Problems. Eine Übernahme des Eigentums bei gleichzeitigem lebenslangem Wohnrecht. Die Zielgruppe soll in dem Flyer auf die bestehende Probleme angesprochen werden und gleichzeitig eine individuelle Lösung angeboten werden, welche eine Mitgliedschaft in dem sozialen Verbund der Genossenschaft ist.
Aufgabenstellung
Der Designer hat hier völlig freie Hand. Es sollte auf die Zielgruppe passen.
Passende Texte soll sich der Designer selbst erdenken.
Nachtrag: Ich habe mittlerweile viele Zuschriften bekommen, dass die Aufgabenstellung sich Texte auszudenken etwas zu allgemein gefasst ist, daher versuche ich hier nochmal etwas Licht in Dunkle zu bringen. Ich habe genauso wenig eine Idee, wie und mit welcher Wortwahl ein Senior auf einfühlsame Weise darauf angesprochen werden soll, ob er nicht sein Haus verkaufen möchte. Meine bisherigen Ideen waren:
'Haben sie schon einmal über den Verkauf ihrer Immobilie nachgedacht? Wussten sie, dass sie ihr Wohneigentum im vollen Umfang weiter nutzen können, ohne weiter die Kosten tragen zu müssen? Sie wollen wissen wie? Rufen sie doch einfach an und ich werde ihnen genau erklären, welche Vorzüge die Mitgliedschaft in einer Genossenschaft mit sich bringt.'
Allerdings erscheint mir das viel zu direkt und ich finde nicht die richtigen Worte diese Personengruppe in dem Maße anzusprechen, wie es nötig wäre, um sie zu einem Anruf zu bewegen. Daher hatte ich gehofft, dass sie hier ein findiger Designer findet, welcher eine bessere kreative Art hat als ich.
Vielleicht ist es die falsche Plattform, vielleicht schaffen wir es nicht die Vorgaben zu spezifizieren. Bilder anzuordnen ist sicher sehr wichtig, auch ist es wichtig aufhellende Elemente einzubringen. Aber wir suchen jemanden der einen Flyer so gestalten kann das der Flyer etwas ausdrückt, das eine Botschaft vermittelt wird, das auf einem Blick der Senior den Wunsch verspürt, bei uns anzurufen. Das heißt viel wichtiger als Bilder, ist der Inhalt der Ansprache. Nicht unbedingt der Inhalt, sondern das WIE. Nochmal: wir wollen ältere Menschen dazu bewegen ihr Eigentum auf Grund von Reperaturrückstau, Überlastung, gesundheitlichen Einschränkungen, finanziellen Schwierigkeiten, zu großem Aufwand in eine Genossenschaft einzubringen. Ds heißt S..

```html
<!DOCTYPE html>
<html lang="de">
<head>
<meta charset="utf-8">
<title>Flyer – Hauseigentum im Ruhestand</title>
<link rel="stylesheet" href="https://fonts.googleapis.com/css2?family=Source+Serif+4:wght@400&family=Open+Sans:ital,wght@0,400;0,600;0,700;1,700&display=swap">
<style>
  :root {
    --paper: #efefef;
    --ink: #111111;
    --teal: #1a8a93;
    --band: #a0bfcb;
    --white: #ffffff;
    --photo-a: #5f7a3e;
    --photo-b: #8aa356;
    --photo-c: #3f5a2b;
  }
  * { margin: 0; padding: 0; box-sizing: border-box; }
  html, body { width: 1200px; height: 3395px; overflow: hidden; background: var(--paper); }
  .flyer { position: relative; width: 1200px; height: 3395px; background: var(--paper); font-family: "Open Sans", sans-serif; color: var(--ink); }

  .headline {
    position: absolute; left: 93px; top: 108px; width: 1060px;
    font-family: "Source Serif 4", serif; font-weight: 400;
    font-size: 128px; line-height: 136px; letter-spacing: 1px;
  }
  .headline .accent { color: var(--teal); }

  .hero-photo {
    position: absolute; left: 0; top: 731px; width: 1200px; height: 740px;
    background: linear-gradient(160deg, var(--photo-c) 0%, var(--photo-a) 45%, var(--photo-b) 100%);
  }

  .section { position: absolute; left: 93px; width: 1040px; }
  .section h2 {
    color: var(--teal); font-weight: 700; font-size: 53px; line-height: 68px;
  }
  .section p {
    margin-top: 14px; font-size: 39px; line-height: 54px; font-weight: 400;
  }
  .section-1 { top: 1540px; }
  .section-2 { top: 2033px; }
  .section-3 { top: 2398px; }

  .contact-band {
    position: absolute; left: 0; top: 2815px; width: 1200px; height: 580px;
    background: var(--band);
  }
  .contact-band h3 {
    position: absolute; left: 93px; top: 44px; width: 1060px;
    font-style: italic; font-weight: 700; font-size: 52px; line-height: 67px;
  }
  .contact-address {
    position: absolute; left: 93px; top: 200px;
    font-size: 44px; line-height: 65px; font-weight: 400;
  }
  .contact-web {
    position: absolute; left: 93px; top: 440px;
    font-size: 38px; line-height: 50px;
  }
  .logo-box {
    position: absolute; left: 716px; top: 233px; width: 484px; height: 164px;
    background: var(--white);
    display: flex; align-items: center; justify-content: center;
    font-size: 38px; letter-spacing: 0.5px;
  }
</style>
</head>
<body>
<div class="flyer">
  <h1 class="headline">Die <span class="accent">risikofreie</span><br>Lösung für Ihr<br>Hauseigentum<br>im Ruhestand.</h1>

  <div class="hero-photo" role="img" aria-label="Foto: fröhliches Seniorenpaar im Garten, der Mann schiebt die lachende Frau in einer Schubkarre"></div>

  <section class="section section-1">
    <h2>Sie sind endlich im wohlverdienten Ruhestand und können nun sorgenfrei in Ihrer Immobilie leben.</h2>
    <p>Ihr Haus hat jedoch so einige Reparaturen nötig? Sie schaffen es gesundheitlich nicht mehr selbst es in Schuss halten oder Ihnen fehlen die finanziellen Mittel dazu?</p>
  </section>

  <section class="section section-2">
    <h2>Ein Verkauf des Hauses kommt für<br>Sie auf keinen Fall in Frage.</h2>
    <p>Geben Sie Ihre Immobilien in eine Gemeinschaft, die sich ohne Risiko oder zusätzliche Kosten um Ihr Heim kümmert.</p>
  </section>

  <section class="section section-3">
    <h2>Profitieren Sie von einer großen Eigentümergemeinschaft, die Sie berät und begleitet.</h2>
    <p>Sie wohnen weiterhin in Ihrem geliebten Zuhause und genießen die schönste Zeit des Lebens.</p>
  </section>

  <footer class="contact-band">
    <h3>Wir beraten Sie am Telefon oder mit Terminvereinbarung bei Ihnen zuhause.</h3>
    <address class="contact-address" style="font-style:normal">
      Genossenschaft xy<br>
      Straße 1 | 13332 xxxxxx<br>
      Telefon 0151 xxxxxxxx
    </address>
    <div class="logo-box">FIRMENLOGO</div>
    <div class="contact-web">wohnbund-lindenhof.de | kontakt@wohnbund-lindenhof.de</div>
  </footer>
</div>
</body>
</html>
```